Digital multi-page Product Brochure

We’re creating a product brochure for our Wood Look Porcelain Pavers. The brochure will show technical details of the pavers, available colors, and applications while also showcasing the advantages of porcelain over wood.
We prefer a clean design aesthetic with appropriate white space incorporated. Because we want the view to appreciate the detail and natural look of the porcelain pavers, we want relatively large color swatches in the available colors section.
Each color swatch section needs the information provided in the guide. The design and layout of these sections is completely open. We do want to see a visual of the paver size in each color swatch section along with the written sizing information.
Mixed use of renderings and actual installation photos. Style and placement of photos is up to designer.
Target Market(s)
Architects and contractors
Industry/Entity Type
Building Materials
Font styles to use
Other font styles liked:
- Outfit - headers, Helvetica for paragraph copy

```html
<!DOCTYPE html>
<html lang="en">
<head>
<meta charset="utf-8">
<title>Terravane Wood Look Porcelain Pavers – Brochure Spreads</title>
<link rel="stylesheet" href="https://fonts.googleapis.com/css2?family=Black+Ops+One&family=Anton&family=Open+Sans:wght@400;600;700&display=swap">
<style>
:root{
  --backdrop:#b3aa9b;
  --paper:#ffffff;
  --charcoal:#3b3b3d;
  --ink:#2b2b2b;
  --rule:#bdbdbd;
  --muted:#555;
  --grey-1:#5c5f63;
  --grey-2:#8d9094;
  --grey-3:#b9bbbe;
  --grey-4:#d3d4d6;
  --black:#1e1e1f;
}
*{box-sizing:border-box;margin:0;padding:0}
html,body{width:1200px;height:486px;overflow:hidden}
body{background:var(--backdrop);font-family:"Open Sans",Helvetica,Arial,sans-serif;color:var(--ink);position:relative}

.page{position:absolute;width:280px;height:198px;background:var(--paper);box-shadow:0 3px 8px rgba(0,0,0,.18);overflow:hidden}
.page--dark{background:var(--charcoal);color:#fff}
.page::before{content:"";position:absolute;left:0;top:0;width:28px;height:3px;background:var(--grey-1)}
.page--dark::before{display:none}

.rail-line{position:absolute;left:27px;top:0;width:.6px;height:60px;background:var(--rule)}
.rail-site,.rail-brand,.rail-year{position:absolute;writing-mode:vertical-rl;transform:rotate(180deg);letter-spacing:.4px;color:inherit}
.rail-site{left:7px;top:12px;font-size:3.6px}
.rail-brand{left:5px;top:86px;font-size:6.5px;font-weight:600;letter-spacing:1.2px}
.rail-year{left:7px;top:177px;font-size:3.8px}
.page-mark{position:absolute;right:17px;bottom:8px;width:5px;height:5px;background:var(--grey-3)}
.page--dark .page-mark{background:#cfcfcf}

.title{position:absolute;font-family:"Black Ops One",Impact,sans-serif;font-size:10.5px;letter-spacing:1.6px;line-height:1;white-space:nowrap}
.subtitle{position:absolute;font-size:4.3px;letter-spacing:1.4px;font-weight:600;white-space:nowrap}
.title--laying{font-family:"Anton",Impact,sans-serif;letter-spacing:-.2px;font-size:10.5px}

.swatch-row{position:absolute;left:34px;display:flex;gap:5.5px}
.swatch{width:33px}
.swatch-tile{width:33px;height:33px}
.swatch-name{font-size:2.6px;font-weight:700;letter-spacing:.5px;margin-top:3px;white-space:nowrap;color:var(--ink)}
.swatch-spec{font-size:2.1px;line-height:1.3;color:var(--muted);text-transform:uppercase}
.size-key{width:33px}
.size-grid{display:grid;grid-template-columns:repeat(3,10px);gap:1.5px;height:33px}
.size-grid span{display:block;height:10px}

.photo{position:absolute}
.caption{position:absolute;font-size:3.6px;font-weight:700;white-space:nowrap}

.body-copy{position:absolute;left:32px;top:50px;width:77px;font-size:3.3px;line-height:1.45;text-align:justify}
.parts{position:absolute;left:135px;top:131px;font-size:1.9px;line-height:5.2px;color:var(--muted)}
</style>
</head>
<body>

<!-- Spread 1: colours A -->
<section class="page" style="left:15px;top:60px">
  <div class="rail-line"></div>
  <span class="rail-site">terravane.com</span><span class="rail-brand">terravane</span><span class="rail-year">2025</span>
  <h2 class="title" style="left:34px;top:31px">APPLICATIONS</h2>
  <p class="subtitle" style="left:35px;top:45px">COLOURS AND SIZES</p>
  <div class="swatch-row" style="top:51px">
    <div class="swatch"><div class="swatch-tile" role="img" aria-label="Dune porcelain paver surface" style="background:linear-gradient(90deg,#6e6a62,#8a857b,#66625a)"></div><p class="swatch-name">DUNE</p><p class="swatch-spec">23 1/2" x 23 1/2"<br>V3 high shade<br>&amp; texture variation</p></div>
    <div class="swatch"><div class="swatch-tile" role="img" aria-label="Ember porcelain paver surface" style="background:linear-gradient(90deg,#8a5037,#a0644a,#84492f)"></div><p class="swatch-name">EMBER</p><p class="swatch-spec">16"x48"<br>V3 high shade<br>&amp; texture variation</p></div>
    <div class="swatch"><div class="swatch-tile" role="img" aria-label="Loam porcelain paver surface" style="background:linear-gradient(90deg,#6a5d52,#7c6e62,#645649)"></div><p class="swatch-name">LOAM</p><p class="swatch-spec">16"x48"<br>V3 high shade<br>&amp; texture variation</p></div>
    <div class="swatch"><div class="swatch-tile" role="img" aria-label="Shoreline porcelain paver surface" style="background:linear-gradient(90deg,#b9b7b2,#cfcdc8,#aeaca6)"></div><p class="swatch-name">SHORELINE</p><p class="swatch-spec">23 1/2" x 47 1/8"<br>11 1/2" x 47 1/8"<br>V3 high shade<br>&amp; texture variation</p></div>
    <div class="swatch"><div class="swatch-tile" role="img" aria-label="Calm Sand porcelain paver surface" style="background:linear-gradient(90deg,#a06a42,#b98154,#9a6238)"></div><p class="swatch-name">CALM SAND</p><p class="swatch-spec">12"x48"<br>V3 high shade<br>&amp; texture variation</p></div>
    <div class="size-key"><div class="size-grid"><span style="background:var(--grey-1)"></span><span style="background:var(--grey-3)"></span><span style="background:var(--grey-2)"></span><span style="background:var(--grey-3)"></span><span style="background:var(--grey-2)"></span><span style="background:var(--grey-1)"></span><span style="background:var(--grey-2)"></span><span style="background:var(--grey-1)"></span><span style="background:var(--grey-4)"></span></div><p class="swatch-spec" style="margin-top:3px">V3 high shade<br>&amp; texture variation</p></div>
  </div>
  <div class="swatch-row" style="top:111px">
    <div class="swatch"><div class="swatch-tile" role="img" aria-label="Bosco Pallido porcelain paver surface" style="background:linear-gradient(90deg,#d8d2c7,#e6e1d8,#cfc8bb)"></div><p class="swatch-name">BOSCO PALLIDO</p><p class="swatch-spec">16"x32"<br>V3 high shade<br>&amp; texture variation</p></div>
    <div class="swatch"><div class="swatch-tile" role="img" aria-label="Rubicon porcelain paver surface" style="background:linear-gradient(90deg,#6e3f2b,#85503a,#683926)"></div><p class="swatch-name">RUBICON</p><p class="swatch-spec">23 1/2" x 23 1/2"<br>47 1/8" x 23 1/2"<br>V4 very high shade &amp;<br>texture variation &amp;<br>random color<br>differences</p></div>
    <div class="swatch"><div class="swatch-tile" role="img" aria-label="Honey porcelain paver surface" style="background:linear-gradient(90deg,#a47a4e,#b88c5e,#9b7045)"></div><p class="swatch-name">HONEY</p><p class="swatch-spec">16"x48"<br>V3 high shade<br>&amp; texture variation</p></div>
    <div class="swatch"><div class="swatch-tile" role="img" aria-label="Rosea porcelain paver surface" style="background:linear-gradient(90deg,#c29a7b,#d0ab8e,#b98f70)"></div><p class="swatch-name">ROSEA</p><p class="swatch-spec">11 13/16" x 47 2/8"<br>V3 high shade<br>&amp; texture variation</p></div>
    <div class="swatch"><div class="swatch-tile" role="img" aria-label="Aurum porcelain paver surface" style="background:linear-gradient(90deg,#c39867,#d4ab7c,#bb8e5e)"></div><p class="swatch-name">AURUM</p><p class="swatch-spec">11 13/16" x 47 2/8"<br>V4 very high shade &amp;<br>texture variation &amp;<br>random color<br>differences</p></div>
    <div class="size-key"><div class="size-grid"><span style="background:var(--grey-1)"></span><span style="background:var(--black)"></span><span style="background:var(--grey-2)"></span><span style="background:var(--grey-3)"></span><span style="background:var(--grey-1)"></span><span style="background:var(--black)"></span><span style="background:var(--black)"></span><span style="background:var(--grey-3)"></span><span style="background:var(--grey-1)"></span></div><p class="swatch-spec" style="margin-top:3px">V4 very high shade &amp;<br>texture variation &amp;<br>random color<br>differences</p></div>
  </div>
  <span class="page-mark"></span>
</section>

<!-- Spread 2: colours B -->
<section class="page" style="left:306px;top:60px;width:283px">
  <div class="rail-line"></div>
  <span class="rail-site">terravane.com</span><span class="rail-brand">terravane</span><span class="rail-year">2025</span>
  <h2 class="title" style="left:39px;top:31px">APPLICATIONS</h2>
  <p class="subtitle" style="left:40px;top:45px">COLOURS AND SIZES</p>
  <div class="swatch-row" style="top:51px;left:39px;gap:7px">
    <div class="swatch"><div class="swatch-tile" role="img" aria-label="Ridgeline Nut porcelain paver surface" style="background:linear-gradient(90deg,#5e5248,#74665a,#574b41)"></div><p class="swatch-name">RIDGELINE NUT</p><p class="swatch-spec">47 1/8" x 7 3/4"<br>47 1/8" x 15 5/8"<br>10 1/2" x 72"<br>V4 very high shade<br>&amp; random color</p></div>
    <div class="swatch"><div class="swatch-tile" role="img" aria-label="Fernvale porcelain paver surface" style="background:linear-gradient(90deg,#a99c8b,#bbaf9f,#a09281)"></div><p class="swatch-name">FERNVALE</p><p class="swatch-spec">23 1/2" x 47 1/8"<br>11 ½" x 47 1/8"<br>V3 high shade<br>&amp; texture variation</p></div>
    <div class="swatch"><div class="swatch-tile" role="img" aria-label="Linden Mist porcelain paver surface" style="background:linear-gradient(90deg,#a8998a,#b9ab9c,#9f8f7f)"></div><p class="swatch-name">LINDEN MIST</p><p class="swatch-spec">23 1/2" x 47 1/8"<br>11 ½" x 47 1/8"<br>V3 high shade<br>&amp; texture variation</p></div>
    <div class="swatch"><div class="swatch-tile" role="img" aria-label="Solano porcelain paver surface" style="background:linear-gradient(90deg,#9d9a91,#b1aea5,#939087)"></div><p class="swatch-name">SOLANO</p><p class="swatch-spec">47 1/8" x 15 5/8"<br>47 1/8" x 7 3/4"<br>10 1/2" x 72"<br>V3 high shade<br>&amp; texture variation</p></div>
    <div class="swatch"><div class="swatch-tile" role="img" aria-label="Highmoor porcelain paver surface" style="background:linear-gradient(90deg,#8f7c62,#a28e72,#877359)"></div><p class="swatch-name">HIGHMOOR</p><p class="swatch-spec">16"x48"<br>V3 high shade<br>&amp; texture variation</p></div>
    <div class="size-key"><div class="size-grid"><span style="background:var(--grey-1)"></span><span style="background:var(--grey-3)"></span><span style="background:var(--grey-2)"></span><span style="background:var(--grey-3)"></span><span style="background:var(--grey-2)"></span><span style="background:var(--grey-1)"></span><span style="background:var(--grey-2)"></span><span style="background:var(--grey-1)"></span><span style="background:var(--grey-4)"></span></div><p class="swatch-spec" style="margin-top:3px">V3 high shade<br>&amp; texture variation</p></div>
  </div>
  <div class="swatch-row" style="top:110px;left:39px;gap:7px">
    <div class="swatch"><div class="swatch-tile" role="img" aria-label="Valmora porcelain paver surface" style="background:linear-gradient(90deg,#a59d92,#b7afa4,#9c9488)"></div><p class="swatch-name">VALMORA</p><p class="swatch-spec">47 1/8" x 15 5/8"<br>47 1/8" x 7 3/4"<br>10 1/2" x 72"<br>V3 high shade<br>&amp; texture variation</p></div>
    <div class="swatch"><div class="swatch-tile" role="img" aria-label="Cortena porcelain paver surface" style="background:linear-gradient(90deg,#8f7a5e,#a38d70,#857055)"></div><p class="swatch-name">CORTENA</p><p class="swatch-spec">23 1/2" x 23 1/2"<br>V4 very high shade &amp;<br>texture variation &amp;<br>random color<br>differences</p></div>
    <div class="swatch"><div class="swatch-tile" role="img" aria-label="Grainline Brown porcelain paver surface" style="background:linear-gradient(90deg,#6e5f52,#857466,#66574a)"></div><p class="swatch-name">GRAINLINE - BROWN</p><p class="swatch-spec">23 1/2" x 23 1/2"<br>V4 very high shade &amp;<br>texture variation &amp;<br>random color<br>differences</p></div>
    <div class="swatch"><div class="swatch-tile" role="img" aria-label="Grainline Ivory porcelain paver surface" style="background:linear-gradient(90deg,#b7b0a7,#c9c3ba,#aea79d)"></div><p class="swatch-name">GRAINLINE - IVORY</p><p class="swatch-spec">23 1/2" x 23 1/2"<br>V4 very high shade &amp;<br>texture variation &amp;<br>random color<br>differences</p></div>
    <div class="swatch"><div class="swatch-tile" role="img" aria-label="Grainline Grey porcelain paver surface" style="background:linear-gradient(90deg,#8c877d,#a09a90,#837e74)"></div><p class="swatch-name">GRAINLINE - GREY</p><p class="swatch-spec">23 1/2" x 23 1/2"<br>V4 very high shade &amp;<br>texture variation &amp;<br>random color<br>differences</p></div>
    <div class="size-key"><div class="size-grid"><span style="background:var(--grey-1)"></span><span style="background:var(--black)"></span><span style="background:var(--grey-2)"></span><span style="background:var(--grey-3)"></span><span style="background:var(--grey-1)"></span><span style="background:var(--black)"></span><span style="background:var(--black)"></span><span style="background:var(--grey-3)"></span><span style="background:var(--grey-1)"></span></div><p class="swatch-spec" style="margin-top:3px">V4 very high shade &amp;<br>texture variation &amp;<br>random color<br>differences</p></div>
  </div>
  <span class="page-mark"></span>
</section>

<!-- Spread 3: laying options -->
<section class="page" style="left:612px;top:60px;width:278px">
  <div class="rail-line"></div>
  <span class="rail-site">terravane.com</span><span class="rail-brand">terravane</span><span class="rail-year">2025</span>
  <h2 class="title title--laying" style="left:39px;top:31px">LAYING OPTIONS</h2>
  <p class="subtitle" style="left:39px;top:45px">INSTALLATION OPTIONS</p>
  <div class="photo" role="img" aria-label="Pavers on pedestals along a glazed terrace" style="left:49px;top:53px;width:65px;height:50px;background:linear-gradient(180deg,#6d7479,#8c7a63 65%,#7a5c44)"></div>
  <div class="photo" role="img" aria-label="Pavers laid on sand and gravel in a garden lounge" style="left:117px;top:53px;width:65px;height:50px;background:linear-gradient(160deg,#5d6b45,#8d8d86 55%,#6c6c68)"></div>
  <div class="photo" role="img" aria-label="Pavers laid on a concrete slab" style="left:186px;top:53px;width:68px;height:50px;background:linear-gradient(135deg,#9fa2a3,#c9cbcc 50%,#a4a6a7)"></div>
  <span class="caption" style="left:49px;top:106px">Pedestals</span>
  <span class="caption" style="left:117px;top:106px">Sand &amp; Gravel</span>
  <span class="caption" style="left:186px;top:106px">Concrete slab</span>
  <div class="photo" role="img" aria-label="Pavers set on a thinset bed in a plaza" style="left:49px;top:115px;width:65px;height:51px;background:linear-gradient(180deg,#5b6366,#a9acac 55%,#8b8e8c)"></div>
  <div class="photo" role="img" aria-label="Stepping pavers set into lawn and turf" style="left:117px;top:115px;width:65px;height:51px;background:linear-gradient(160deg,#4c6434,#7d8a5e 55%,#8a6a48)"></div>
  <span class="caption" style="left:49px;top:170px">Thinset bed</span>
  <span class="caption" style="left:117px;top:170px">lawn &amp; turf</span>
  <span class="page-mark"></span>
</section>

<!-- Spread 4: project inspiration dark -->
<section class="page page--dark" style="left:903px;top:60px;width:284px">
  <span class="rail-site">terravane.com</span><span class="rail-brand">terravane</span><span class="rail-year">2025</span>
  <div class="photo" role="img" aria-label="Rooftop boardwalk terrace beside a glass tower" style="left:23px;top:0;width:65px;height:172px;background:linear-gradient(180deg,#8fa6bb,#6d6a66 45%,#7a5a45)"></div>
  <div class="photo" role="img" aria-label="Rooftop lounge with turf and city skyline at dusk" style="left:91px;top:0;width:69px;height:172px;background:linear-gradient(180deg,#8aa3b8,#c9a48d 30%,#5f7a4a 55%,#8a6f5c)"></div>
  <div class="photo" role="img" aria-label="Brick building terrace with wood look pavers" style="left:162px;top:0;width:69px;height:172px;background:linear-gradient(180deg,#5b4a44,#7e5646 45%,#a0806a)"></div>
  <h2 class="title" style="right:15px;top:33px;text-align:right;color:#fff;line-height:1.05">PROJECT<br>INSPIRATION</h2>
  <span class="page-mark"></span>
</section>

<!-- Spread 5: colours C -->
<section class="page" style="left:13px;top:280px;width:279px;height:197px">
  <div class="rail-line"></div>
  <span class="rail-site">terravane.com</span><span class="rail-brand">terravane</span><span class="rail-year">2025</span>
  <h2 class="title" style="left:39px;top:33px">APPLICATIONS</h2>
  <p class="subtitle" style="left:40px;top:45px">COLOURS AND SIZES</p>
  <div class="swatch-row" style="top:51px;left:39px;gap:6px">
    <div class="swatch"><div class="swatch-tile" role="img" aria-label="Hearth porcelain paver surface" style="background:linear-gradient(90deg,#6e655b,#857b70,#655c52)"></div><p class="swatch-name">HEARTH</p><p class="swatch-spec">16"x48"<br>V3, high shade<br>&amp; texture variation</p></div>
    <div class="swatch"><div class="swatch-tile" role="img" aria-label="Umber porcelain paver surface" style="background:linear-gradient(90deg,#6b5b4c,#7f6d5d,#625244)"></div><p class="swatch-name">UMBER</p><p class="swatch-spec">16"x48"<br>V3, high shade<br>&amp; texture variation</p></div>
    <div class="swatch"><div class="swatch-tile" role="img" aria-label="Ridgeline Oak porcelain paver surface" style="background:linear-gradient(90deg,#b39a7c,#c5ad90,#aa9072)"></div><p class="swatch-name">RIDGELINE OAK</p><p class="swatch-spec">47 1/8" x 7 3/4"<br>47 1/8" x 15 5/8"<br>10 1/2" x 72"<br>V4, very high shade &amp; texture<br>variation &amp; random color</p></div>
  </div>
  <span class="page-mark"></span>
</section>

<!-- Spread 6: installation -->
<section class="page" style="left:305px;top:280px;width:284px;height:197px">
  <div class="rail-line"></div>
  <span class="rail-site">terravane.com</span><span class="rail-brand">terravane</span><span class="rail-year">2025</span>
  <h2 class="title" style="right:29px;top:31px;text-align:right">INSTALLATION</h2>
  <p class="subtitle" style="right:29px;top:43px">INSTALLATION AND APPLICATION</p>
  <p class="body-copy">Assuming it's not a large area and the slope for drainage is around the typical 2-2.5%, you can easily lay Terravane porcelain pavers over concrete surfaces using our 1/4" or 3/8" high rubber support pads placed under each corner of the pavers. For more information on how to install porcelain pavers over rubber support pads</p>
  <div class="photo" role="img" aria-label="Rendering of pavers raised on adjustable pedestals" style="left:115px;top:50px;width:140px;height:75px;background:linear-gradient(180deg,#6f7f92,#dfe3ea 35%,#a9b4c6 70%,#8e9aae)"></div>
  <div class="photo" role="img" aria-label="Exploded diagram of an adjustable pedestal" style="left:95px;top:131px;width:33px;height:41px;background:linear-gradient(180deg,#4a4a4a,#1f1f1f)"></div>
  <p class="parts">Clip on cap with spacer tabs<br>Tapped root head for wind uplift system<br>Screwed column<br>Locking ring<br>Base with screwed column</p>
  <div class="photo" role="img" aria-label="Close-up of a pedestal supporting a paver edge" style="left:171px;top:127px;width:84px;height:42px;background:linear-gradient(180deg,#dfe3e7,#a8b3bd 55%,#7d8993)"></div>
  <span class="page-mark"></span>
</section>

<!-- Spread 7: project inspiration light -->
<section class="page" style="left:612px;top:279px;width:278px;height:198px">
  <div class="rail-line"></div>
  <span class="rail-site">terravane.com</span><span class="rail-brand">terravane</span><span class="rail-year">2025</span>
  <h2 class="title" style="left:38px;top:33px;line-height:1.05">PROJECT<br>INSPIRATION</h2>
  <div class="photo" role="img" aria-label="Aerial view of a terrace lounge and dining area on light wood look pavers" style="left:156px;top:17px;width:86px;height:94px;background:linear-gradient(160deg,#3e3d3b,#a09c95 35%,#c9c4bb 70%,#8f8a82)"></div>
  <div class="photo" role="img" aria-label="Garden patio with outdoor seating on wood look pavers" style="left:27px;top:111px;width:112px;height:87px;background:linear-gradient(180deg,#4d6a3a,#6f7e57 40%,#b59f86 70%,#a08a72)"></div>
  <span class="page-mark"></span>
</section>

<!-- Spread 8: project inspiration dark -->
<section class="page page--dark" style="left:903px;top:279px;width:284px;height:198px">
  <span class="rail-site">terravane.com</span><span class="rail-brand">terravane</span><span class="rail-year">2025</span>
  <div class="photo" role="img" aria-label="Covered restaurant terrace with wood look pavers" style="left:27px;top:38px;width:115px;height:73px;background:linear-gradient(180deg,#e9e9e7,#5a4e46 35%,#8f6f58 75%,#7a5d48)"></div>
  <div class="photo" role="img" aria-label="Penthouse terrace lounge overlooking a city" style="left:113px;top:71px;width:171px;height:95px;background:linear-gradient(180deg,#b9c8d6,#8a9aa6 35%,#7e5e48 65%,#6b4c39)"></div>
  <span class="page-mark"></span>
</section>

</body>
</html>
```